business card for a massage therapy practice named 'Meadow and Willow Massage Studio'

I really need a trendy, yet easy on the eyes business card to complement my logo. Ideally with some gold or rose gold foil work.

My uploaded file of the logo I have in horizontal but I have a vertical version as well. Another color that is used in the website is a blush pink here and there. I'd like to see some trendy tropical leaves in the design.

```html
<!DOCTYPE html>
<html lang="en">
<head>
<meta charset="utf-8">
<title>Meadow and Willow Massage Studio – Business Card</title>
<link href="https://fonts.googleapis.com/css2?family=Cormorant+SC:wght@600&family=Josefin+Sans:wght@400;600&display=swap" rel="stylesheet">
<style>
  :root {
    --backdrop: #ece8e3;
    --card-white: #f7f6f4;
    --leaf-navy: #2c3850;
    --leaf-deep: #2f5d55;
    --leaf-mid: #4f9a7c;
    --leaf-light: #9fd3a6;
    --ink: #23262b;
    --ink-soft: #4a4d52;
    --gold: #b9a26e;
    --blush: #d98f8c;
    --blush-edge: #e7b9b4;
  }
  * { box-sizing: border-box; margin: 0; padding: 0; }
  html, body { width: 1200px; height: 800px; overflow: hidden; }
  body {
    background: var(--backdrop);
    display: flex;
    align-items: center;
    justify-content: center;
    gap: 60px;
    font-family: "Josefin Sans", sans-serif;
    color: var(--ink);
  }
  .card {
    width: 520px;
    height: 298px;
    position: relative;
    overflow: hidden;
    background: var(--card-white);
    box-shadow: 0 10px 30px rgba(40, 35, 30, 0.18);
  }
  .leaf-pattern {
    position: absolute;
    background:
      radial-gradient(ellipse at 25% 30%, rgba(159, 211, 166, 0.55), transparent 45%),
      radial-gradient(ellipse at 75% 65%, rgba(79, 154, 124, 0.6), transparent 50%),
      radial-gradient(ellipse at 60% 15%, rgba(47, 93, 85, 0.7), transparent 40%),
      linear-gradient(135deg, var(--leaf-deep), var(--leaf-navy) 55%, var(--leaf-deep));
  }

  /* Front */
  .card-front .leaf-pattern { inset: 0; }
  .front-frame {
    position: absolute;
    left: 120px; top: 74px;
    width: 296px; height: 150px;
    border: 3px solid var(--card-white);
  }
  .front-panel {
    position: absolute;
    left: 108px; top: 62px;
    width: 296px; height: 150px;
    background: var(--card-white);
    display: flex;
    align-items: center;
    justify-content: center;
  }

  /* Wordmark */
  .wordmark {
    display: flex;
    align-items: center;
    gap: 12px;
  }
  .wordmark-dot {
    width: 26px; height: 26px;
    border-radius: 50%;
    background: var(--gold);
    flex: none;
  }
  .wordmark-name {
    font-family: "Josefin Sans", sans-serif;
    font-weight: 400;
    color: var(--ink);
    font-size: 20px;
    line-height: 1.2;
    letter-spacing: 0.06em;
    text-transform: uppercase;
  }

  /* Back */
  .card-back .leaf-pattern {
    left: 0; top: 0; bottom: 0;
    width: 196px;
  }
  .back-edge {
    position: absolute;
    left: 196px; top: 0; bottom: 0;
    width: 2px;
    background: var(--blush-edge);
  }
  .back-content {
    position: absolute;
    left: 198px; right: 0; top: 0; bottom: 0;
    padding: 26px 24px 20px 38px;
  }
  .back-content .wordmark-name { font-size: 18px; }
  .holder {
    margin-top: 26px;
    padding-left: 20px;
    text-align: center;
    width: 250px;
  }
  .holder-name {
    font-family: "Cormorant SC", serif;
    font-weight: 600;
    font-size: 21px;
    letter-spacing: 0.04em;
  }
  .holder-title {
    font-size: 10px;
    color: var(--ink-soft);
    margin-top: 1px;
  }
  .contact-list {
    list-style: none;
    margin-top: 16px;
    padding-left: 14px;
  }
  .contact-item {
    display: flex;
    align-items: center;
    gap: 10px;
    font-size: 11.5px;
    color: var(--ink-soft);
    height: 19px;
  }
  .contact-icon {
    width: 12px; height: 12px;
    flex: none;
  }
</style>
</head>
<body>

<section class="card card-front" aria-label="Card front">
  <div class="leaf-pattern" role="img" aria-label="Tropical palm leaf pattern in green on navy"></div>
  <div class="front-frame"></div>
  <div class="front-panel">
    <div class="wordmark">
      <span class="wordmark-dot"></span>
      <span class="wordmark-name">Meadow &amp; Willow<br>Massage Studio</span>
    </div>
  </div>
</section>

<section class="card card-back" aria-label="Card back">
  <div class="leaf-pattern" role="img" aria-label="Tropical palm leaf pattern in green on navy"></div>
  <div class="back-edge"></div>
  <div class="back-content">
    <div class="wordmark">
      <span class="wordmark-dot"></span>
      <span class="wordmark-name">Meadow &amp; Willow<br>Massage Studio</span>
    </div>
    <div class="holder">
      <p class="holder-name">Elena Marsh</p>
      <p class="holder-title">Licensed Massage Therapist</p>
    </div>
    <ul class="contact-list">
      <li class="contact-item">
        <svg class="contact-icon" viewBox="0 0 12 12" aria-hidden="true"><rect width="12" height="12" rx="2" fill="var(--blush)"/><path d="M3.6 2.8l1.2 1.3-.6 1c.5 1 1.2 1.7 2.2 2.2l1-.6 1.3 1.2-.7 1.1C5.6 8.8 3.2 6.4 2.9 3.6z" fill="#fff"/></svg>
        555.014.2287
      </li>
      <li class="contact-item">
        <svg class="contact-icon" viewBox="0 0 12 12" aria-hidden="true"><rect width="12" height="12" rx="2" fill="var(--blush)"/><path d="M6 2.6L2.6 5.6h1v3.6h1.9V7.2h1v2h1.9V5.6h1z" fill="#fff"/></svg>
        www.meadowandwillow.com
      </li>
      <li class="contact-item">
        <svg class="contact-icon" viewBox="0 0 12 12" aria-hidden="true"><rect width="12" height="12" rx="2" fill="var(--blush)"/><rect x="2.5" y="3.5" width="7" height="5" fill="none" stroke="#fff" stroke-width="0.9"/><path d="M2.5 3.5L6 6.4l3.5-2.9" fill="none" stroke="#fff" stroke-width="0.9"/></svg>
        meadowandwillow@mailbox.com
      </li>
      <li class="contact-item">
        <svg class="contact-icon" viewBox="0 0 12 12" aria-hidden="true"><rect width="12" height="12" rx="2" fill="var(--blush)"/></svg>
        @meadowandwillow
      </li>
      <li class="contact-item">
        <svg class="contact-icon" viewBox="0 0 12 12" aria-hidden="true"><rect width="12" height="12" rx="2" fill="var(--blush)"/></svg>
        @meadowandwillow
      </li>
    </ul>
  </div>
</section>

</body>
</html>
```